Zestbite Site

I would like to do a blog for food lovers. The name of the blog is BiteZest. I want to build something like Marcus Fennimore and Tobias Wrenfield. Something cool and different. In this blog i need: Place for pictures, videos, instagram connection, plain square Linked to see fans wich like the blog on plain square....

Reason: I need more options of design.

Requirements
Nice to have
• - plain square link
- Instagram
- Something with foursquare

```html
<!DOCTYPE html>
<html lang="en">
<head>
<meta charset="utf-8">
<title>Zestbite Blog</title>
<link href="https://fonts.googleapis.com/css2?family=Source+Sans+3:wght@300;400;600&family=Arimo:wght@400&display=swap" rel="stylesheet">
<style>
:root{
  --teal:#0aa6c6;
  --teal-dark:#0789a6;
  --title:#1296b0;
  --ink:#2b2b2b;
  --muted:#5a5a5a;
  --bar:#151515;
  --side:#4b4b4b;
  --side-line:#333;
  --panel:#efefef;
  --post-head:#dcdcdc;
  --post-meta:#e4e4e4;
  --post-body:#eaeaea;
  --post-foot:#bcbcbc;
  --link:#1180b8;
  --privacy:#7a0f86;
}
*{box-sizing:border-box;margin:0;padding:0}
html,body{width:1012px;height:1200px;overflow:hidden}
body{background:#d9d9d9;font-family:"Source Sans 3",sans-serif;color:var(--ink)}
.page{position:relative;width:1012px;height:1200px}
.header{position:absolute;left:0;top:0;width:1012px;height:194px;background:linear-gradient(#e6e6e6,#d3d3d3)}
.brand{position:absolute;left:10px;top:0;width:220px;height:178px;background:linear-gradient(#fdfdfd,#e9e9e9);
  clip-path:polygon(0 0,100% 0,82% 100%,0 100%);border-radius:0 0 0 8px}
.brand-dot{position:absolute;left:60px;top:40px;width:70px;height:70px;border-radius:50%;background:#e23c7e}
.brand-name{position:absolute;left:22px;top:112px;font-weight:300;font-size:36px;letter-spacing:1px;color:#555;text-transform:uppercase}
.social{position:absolute;left:843px;top:15px;display:flex;gap:5px}
.social span{width:32px;height:32px;border-radius:4px;background:linear-gradient(#8a8a8a,#5c5c5c)}
.nav{position:absolute;left:203px;top:62px;width:783px;height:58px;background:linear-gradient(#2a2a2a,var(--bar));border-radius:4px;
  display:flex;align-items:center;padding-left:12px}
.nav a{color:#fff;text-decoration:none;font-size:18px;padding:0 18px;line-height:58px;border-right:1px solid #333}
.nav a.current{color:var(--teal)}
.nav a:last-child{border:0}
.main{position:absolute;left:10px;top:207px;width:976px;height:907px;background:var(--panel);border:1px solid #cfcfcf}
.box-head{height:52px;background:var(--teal);border:2px solid #0a7f99;display:flex;align-items:center;padding-left:14px;gap:12px;
  color:#fff;font-size:25px;font-weight:600}
.categories{position:absolute;left:19px;top:20px;width:304px}
.cat-list{list-style:none;margin-top:8px}
.cat-list li{height:38px;background:var(--side);border-bottom:1px solid var(--side-line);color:#fff;font-size:16px;display:flex;align-items:center;gap:8px;padding-left:14px}
.cat-list li.active{background:linear-gradient(#16bbd9,var(--teal-dark))}
.latest{position:absolute;left:19px;top:444px;width:304px}
.talk{background:#f7f7f7;border:1px solid #d2d2d2;border-top:0}
.talk article{height:128px;border-bottom:1px solid #d6d6d6;padding:8px 14px;position:relative}
.talk article:last-child{border-bottom:0}
.talk h3{font-family:Arimo,sans-serif;font-weight:400;font-size:16px}
.talk p{font-family:Arimo,sans-serif;font-size:12px;line-height:21px;color:var(--muted);margin-top:4px}
.talk .meta{font-family:Arimo,sans-serif;font-size:12px;margin-top:4px}
.talk .meta a{color:var(--link);text-decoration:none;margin-right:18px}
.count{position:absolute;right:14px;bottom:10px;width:24px;height:20px;border-radius:10px;background:#c5d3d8;font-size:11px;text-align:center;line-height:20px;font-family:Arimo,sans-serif}
.posts{position:absolute;left:338px;top:20px;width:616px}
.post{height:277px;margin-bottom:16px;border:1px solid #d0d0d0}
.post h2{height:55px;background:var(--post-head);color:var(--title);font-weight:600;font-size:25px;padding:12px 13px}
.post .meta{height:36px;background:var(--post-meta);border-top:1px solid #fff;border-bottom:1px solid #c9c9c9;font-size:15px;padding:7px 13px}
.post .meta a{color:var(--link);text-decoration:none}
.post .body{height:149px;background:var(--post-body);display:flex;padding:11px 14px;gap:16px}
.photo{flex:0 0 183px;height:130px;background:#fff;padding:5px;border-radius:3px}
.photo div{width:100%;height:100%;border-radius:3px}
.post .body p{font-family:Arimo,sans-serif;font-size:12px;line-height:21px;color:var(--muted)}
.post .foot{height:35px;background:var(--post-foot);position:relative}
.more{position:absolute;right:0;top:0;height:35px;width:106px;background:linear-gradient(#5a5a5a,#2e2e2e);color:#fff;font-size:15px;
  line-height:35px;padding-left:28px;clip-path:polygon(14px 0,100% 0,100% 100%,14px 100%,0 50%)}
.footer{position:absolute;left:10px;top:1113px;width:976px;height:87px;background:linear-gradient(#fafafa,#dcdcdc);
  border-radius:0 0 40px 40px;text-align:center;font-size:13px;padding-top:16px;line-height:22px}
.footer .privacy{color:var(--privacy)}
</style>
</head>
<body>
<div class="page">
  <header class="header">
    <div class="brand"><span class="brand-dot"></span><span class="brand-name">Zestbite</span></div>
    <div class="social" aria-label="Social links"><span></span><span></span><span></span><span></span></div>
    <nav class="nav">
      <a class="current">Home</a><a>About Us</a><a>foods</a><a>Services</a><a>Products</a><a>Contact Us</a>
    </nav>
  </header>

  <main class="main">
    <section class="categories">
      <div class="box-head"><svg width="38" height="30" viewBox="0 0 38 30"><path d="M2 12h30a15 12 0 0 1-30 0z" fill="#6b3d1f"/><path d="M10 11L36 2M14 11L37 6" stroke="#3a2414" stroke-width="2"/></svg>Categories</div>
      <ul class="cat-list">
        <li class="active">➔ Raitas and Salads</li><li>➔ Beverages</li><li>➔ Breads</li><li>➔ Curries with Gravy</li><li>➔ Rice</li>
        <li>➔ Daal and Beans</li><li>➔ Cakes and Bakes</li><li>➔ Chutneys and Dips</li><li>➔ Indian Sweets</li>
      </ul>
    </section>

    <section class="latest">
      <div class="box-head"><svg width="38" height="30" viewBox="0 0 38 30"><path d="M2 12h30a15 12 0 0 1-30 0z" fill="#6b3d1f"/><path d="M10 11L36 2M14 11L37 6" stroke="#3a2414" stroke-width="2"/></svg>Latest Talk</div>
      <div class="talk">
        <article><h3>Eating Out</h3><p>There are many variations of passages of Lorem Ipsum available, but the majority have suffered alteration in some form,</p><div class="meta"><a>Lorem Ipsum</a>07:28 PM</div><span class="count">10</span></article>
        <article><h3>Food</h3><p>There are many variations of passages of Lorem Ipsum available, but the majority have suffered alteration in some form,</p><div class="meta"><a>Lorem Ipsum</a>07:28 PM</div><span class="count">10</span></article>
        <article><h3>Drinks</h3><p>There are many variations of passages of Lorem Ipsum available, but the majority have suffered alteration in some form,</p><div class="meta"><a>Lorem Ipsum</a>07:28 PM</div><span class="count">10</span></article>
      </div>
    </section>

    <section class="posts">
      <article class="post">
        <h2>Lorem Ipsum is simply dummy text of the printing</h2>
        <div class="meta">Posted on Jun 18th 2012. Tags: <a>Lorem Ipsum</a></div>
        <div class="body"><div class="photo"><div role="img" aria-label="Toasted sandwich with tomato and lettuce" style="background:linear-gradient(#c9a36a,#b0462d 55%,#e9dcc4)"></div></div>
          <p>Contrary to popular belief, Lorem Ipsum is not simply random text. It has roots in a piece of classical Latin literature from 45 BC, making it over 2000 years old. Harold Whitcombe, a Latin professor at Ashgrove College in Vermont, looked up one of the more obscure Latin words, consectetur, from a Lorem Ipsum passage, and going through the cites of the word in classical literature,</p></div>
        <div class="foot"><span class="more">Read More</span></div>
      </article>
      <article class="post">
        <h2>Lorem Ipsum is simply dummy text of the printing</h2>
        <div class="meta">Posted on Jun 18th 2012. Tags: <a>Lorem Ipsum</a></div>
        <div class="body"><div class="photo"><div role="img" aria-label="Salmon salad with greens and peppers" style="background:linear-gradient(135deg,#5b6b2c,#d77a4c 50%,#4a5a24)"></div></div>
          <p>Contrary to popular belief, Lorem Ipsum is not simply random text. It has roots in a piece of classical Latin literature from 45 BC, making it over 2000 years old. Harold Whitcombe, a Latin professor at Ashgrove College in Vermont, looked up one of the more obscure Latin words, consectetur, from a Lorem Ipsum passage, and going through the cites of the word in classical literature,</p></div>
        <div class="foot"><span class="more">Read More</span></div>
      </article>
      <article class="post">
        <h2>Lorem Ipsum is simply dummy text of the printing</h2>
        <div class="meta">Posted on Jun 18th 2012. Tags: <a>Lorem Itpsum</a></div>
        <div class="body"><div class="photo"><div role="img" aria-label="Roast chicken with rice and green beans" style="background:radial-gradient(circle,#a0552c 30%,#e6d7a8 55%,#8a6a3a)"></div></div>
          <p>Contrary to popular belief, Lorem Ipsum is not simply random text. It has roots in a piece of classical Latin literature from 45 BC, making it over 2000 years old. Harold Whitcombe, a Latin professor at Ashgrove College in Vermont, looked up one of the more obscure Latin words, consectetur, from a Lorem Ipsum passage, and going through the cites of the word in classical literature,</p></div>
        <div class="foot"><span class="more">Read More</span></div>
      </article>
    </section>
  </main>

  <footer class="footer">© 2012 Zestbite Blog<br><span class="privacy">We Value Your Privacy.</span></footer>
</div>
</body>
</html>
```